Hurricane Damage Public Adjuster Billboard

I have created several projects with you and have several great designs. I need to format them into a Billboard for upcoming Hurricane Season. Need done in a month. Im also in process of getting an eye catching and easy to remember 800# Vanity phone number like Call 800-Stormfix or 800- Need Help? My included past Sketch Guild projects will give you an idea of what colors, schemes, and designs I gravitate towards. 3 past Design projects were 1) 2 Logos where I picked the 1st place and the 2nd place and 2) Index Card where I picked the winner as the Index Card and the 2nd place as a Post Card. Point is, I will pick and pay for 2 winners if they're good. This should help to sweeten the pot. Also, please look at my website for ideas that I like:

www.TheClaimWardenGroup.com
I want people to feel that I am the best and highest. Level.

I've been getting a lot of quick half effort designs basically cut & pasting my previous projects. Please don't rush and take your time to be creative. A an example, my Biggest Competitor is Crestline Public Adjusting. Their colors are Black and Gold while mine are Blue, White, and Black with a highlight of Orange if possible. I JUST imported a picture of their BillBoard. I need mine better and BLOW AWAY THEIRS. Terms like "Don't be Victimized Twice ?, Don't let the Hurricane Ruin your Life?". "Get Fairly Paid & Move On" "Our Clients Claims are VIP?
Updates

I'm getting a lot of quick half effort ones. I'd rather you take your time and really put some thoughts and effort into it. My Biggest Competitor is Crestline Public Adjusting. They have black & gold colors, while I have Blue, Black, and white.

It needs to blow theirs away. I have imported their Billboard for comparative purposes.

Guy's,
I'll make it easier for you in what I'm looking for. Please look at the Crestline Billboard picture attached.

1) Put my "Blue Shield" to the left, replacing their logo
2) change color patterns from their (Black, Gold, White) to my color schemes of (Black, Blue, White)
3) I want to see my name where their is:

THE
Claim Warden Group
EXPERT & LOCAL Public Adjusters
"FOR THE POLICYHOLDER!!"

4) to the right, add the A+Rated logo and QTR+ Accredited logo, 5 Star Zentrio Rated logo, 5 Start BLOCKLINK Highly Rated logo, etc..

5) the right side is where you can be creative as I will not have a picture of me there.

"20+ Years of Experience, Recovering Millions for our VIP Clients"

"Your Best, Locally-Based Private Adjuster & Advocate'
"FOR THE POLICYHOLDER!!"

"Don't be victimized Twice!!"

"Don't let the Hurricane Ruin Your Life!!"

This should really help. Also, refer to my website, maybe a couple testimonial fillers?

Thanks all,

marvin@TheClaimWardenGroup.com

Just imported a few awards that would look great to the right side with all the other 5 Star Ratings and accolades.
This right section could be titled like zmy Website:

5 Star Reviews, Ratings & Awards:
4-5 Logos underneath?

Target Market(s)

Coastal place where a Hurricane 🌀 🌀 Hits

Industry/Entity Type

Hurricane Public Insurance Adjuster

Font styles to use
Sans Serif
Other font styles liked:
• Calvera fonts

Colors
0054AA
0677BA
7BADD7
CADEEF
E8F1F8
EE7325
F08F49
F5BC92
FAE3D3
FDF4ED

Requirements
Must have
• Use my past project logos, colors, and schemes to create eye grabbing BillBoard
Nice to have
Should not have
• Not be too busy, must be Easy to Read, Eye Catchy

```html
<!DOCTYPE html>
<html lang="en">
<head>
<meta charset="utf-8">
<title>Storm Damage Alert Billboard</title>
<link href="https://fonts.googleapis.com/css2?family=Montserrat:ital,wght@0,400;0,600;0,700;0,800;1,400&family=Oswald:wght@500&family=Tinos&display=swap" rel="stylesheet">
<style>
  :root {
    --page: #b0b0b0;
    --navy: #0c1e30;
    --navy-deep: #081624;
    --storm: #2a3346;
    --blue: #009ee3;
    --blue-dark: #0054aa;
    --red: #f0141e;
    --orange: #f08f1e;
    --white: #ffffff;
    --ink: #1a1a1a;
    --violet: #5b1fd6;
    --violet-deep: #1a0550;
  }
  * { margin: 0; padding: 0; box-sizing: border-box; }
  html, body { width: 1064px; height: 1200px; overflow: hidden; }
  body { background: var(--page); font-family: "Montserrat", sans-serif; position: relative; }

  .billboard {
    position: absolute; left: 32px; top: 392px; width: 1000px; height: 416px;
    overflow: hidden; box-shadow: 6px 10px 18px rgba(0,0,0,.45);
  }
  .storm-backdrop {
    position: absolute; inset: 0;
    background:
      radial-gradient(ellipse at 62% 45%, #4a5468 0%, rgba(42,51,70,.6) 30%, transparent 60%),
      radial-gradient(ellipse at 95% 20%, #3b4458 0%, transparent 45%),
      linear-gradient(90deg, var(--navy-deep) 0%, var(--navy) 35%, var(--storm) 70%, #1c2638 100%);
  }

  .brand { position: absolute; left: 50px; top: 28px; display: flex; align-items: flex-start; gap: 12px; }
  .brand-mark { width: 52px; height: 52px; border-radius: 50%; background: var(--blue); margin-top: 6px; }
  .brand-text { text-align: center; color: var(--white); }
  .brand-name { font-family: "Tinos", serif; color: var(--blue); font-size: 17px; line-height: 19px; text-transform: uppercase; }
  .brand-tag { font-size: 8.5px; margin-top: 4px; }
  .brand-motto { font-size: 8.5px; font-style: italic; margin-top: 2px; }

  .rating-box {
    position: absolute; left: 316px; top: 31px; width: 140px; height: 71px;
    border: 1px solid #8a8f99; border-radius: 3px; text-align: center; color: var(--white);
    font-family: "Tinos", serif; padding-top: 6px;
  }
  .rating-title { font-family: "Montserrat", sans-serif; font-weight: 700; color: var(--red); font-size: 23px; line-height: 24px; }
  .rating-line { font-size: 10.5px; line-height: 11px; }
  .rating-source { font-size: 5px; line-height: 6px; }

  .headline { position: absolute; left: 57px; top: 126px; display: flex; align-items: center; gap: 16px; }
  .headline-storm { font-family: "Oswald", sans-serif; font-weight: 500; color: var(--red); font-size: 94px; line-height: 80px; letter-spacing: -1px; transform: scaleY(1.06); }
  .headline-alert { font-weight: 800; color: var(--white); font-size: 38px; line-height: 40px; }

  .claims { position: absolute; left: 57px; top: 228px; display: grid; grid-template-columns: 203px 200px; row-gap: 5px; }
  .claim { display: flex; align-items: center; gap: 9px; color: var(--white); font-weight: 600; font-size: 12px; height: 18px; }
  .claim svg { flex: none; }

  .call-bar {
    position: absolute; left: 57px; top: 340px; width: 428px; height: 30px;
    background: var(--white); border-radius: 15px; display: flex; align-items: center;
    padding-left: 8px; font-weight: 700; font-size: 16px; color: var(--ink);
  }
  .call-bar svg { flex: none; }
  .call-word { color: var(--red); margin-left: 10px; }
  .call-num { color: var(--blue); margin-left: 5px; }
  .call-alt { display: flex; align-items: center; margin-left: 16px; }
  .call-or { margin-left: 8px; }
  .call-help { color: var(--orange); margin-left: 5px; }
  .call-pre { color: var(--blue); margin-left: 5px; }

  .website { position: absolute; left: 57px; width: 428px; top: 380px; text-align: center; color: var(--white); font-size: 12px; }
  .website b { color: var(--blue); font-weight: 700; }

  .feature { position: absolute; left: 620px; top: 18px; width: 330px; height: 385px; }
</style>
</head>
<body>
  <div class="billboard">
    <div class="storm-backdrop" role="img" aria-label="Dark storm clouds with lightning over the sky"></div>

    <div class="brand">
      <div class="brand-mark"></div>
      <div class="brand-text">
        <div class="brand-name">The<br>Claim Warden Group</div>
        <div class="brand-tag">INSURANCE CLAIM EXPERTS</div>
        <div class="brand-motto">FOR THE POLICYHOLDER!!</div>
      </div>
    </div>

    <div class="rating-box">
      <div class="rating-title">A+ Rating</div>
      <div class="rating-line">Highest Rating For</div>
      <div class="rating-line">Public Insurance Adjusters</div>
      <div class="rating-source">(Source: ClaimScore)</div>
    </div>

    <div class="headline">
      <div class="headline-storm">STORM</div>
      <div class="headline-alert">DAMAGE<br>ALERT!</div>
    </div>

    <div class="claims">
      <div class="claim"><svg width="10" height="10" viewBox="0 0 10 10"><circle cx="5" cy="5" r="5" fill="#f08f1e"/><path d="M2.7 5.1l1.6 1.6 3-3.2" stroke="#fff" stroke-width="1.3" fill="none"/></svg>Hurricane Damage Claims</div>
      <div class="claim"><svg width="10" height="10" viewBox="0 0 10 10"><circle cx="5" cy="5" r="5" fill="#f08f1e"/><path d="M2.7 5.1l1.6 1.6 3-3.2" stroke="#fff" stroke-width="1.3" fill="none"/></svg>Flood Damage Claims</div>
      <div class="claim"><svg width="10" height="10" viewBox="0 0 10 10"><circle cx="5" cy="5" r="5" fill="#f08f1e"/><path d="M2.7 5.1l1.6 1.6 3-3.2" stroke="#fff" stroke-width="1.3" fill="none"/></svg>Water Damage Claims</div>
      <div class="claim"><svg width="10" height="10" viewBox="0 0 10 10"><circle cx="5" cy="5" r="5" fill="#f08f1e"/><path d="M2.7 5.1l1.6 1.6 3-3.2" stroke="#fff" stroke-width="1.3" fill="none"/></svg>Fire Damage Claims</div>
      <div class="claim"><svg width="10" height="10" viewBox="0 0 10 10"><circle cx="5" cy="5" r="5" fill="#f08f1e"/><path d="M2.7 5.1l1.6 1.6 3-3.2" stroke="#fff" stroke-width="1.3" fill="none"/></svg>Wind Damage Claims</div>
      <div class="claim"><svg width="10" height="10" viewBox="0 0 10 10"><circle cx="5" cy="5" r="5" fill="#f08f1e"/><path d="M2.7 5.1l1.6 1.6 3-3.2" stroke="#fff" stroke-width="1.3" fill="none"/></svg>Mold Growth/Damage Claims</div>
      <div class="claim"><svg width="10" height="10" viewBox="0 0 10 10"><circle cx="5" cy="5" r="5" fill="#f08f1e"/><path d="M2.7 5.1l1.6 1.6 3-3.2" stroke="#fff" stroke-width="1.3" fill="none"/></svg>Roof Damage Claims</div>
      <div class="claim"><svg width="10" height="10" viewBox="0 0 10 10"><circle cx="5" cy="5" r="5" fill="#f08f1e"/><path d="M2.7 5.1l1.6 1.6 3-3.2" stroke="#fff" stroke-width="1.3" fill="none"/></svg>Hail Damage Claims</div>
    </div>

    <div class="call-bar">
      <svg width="22" height="22" viewBox="0 0 22 22"><circle cx="11" cy="11" r="10" fill="none" stroke="#0c1e30" stroke-width="2"/><path d="M7.5 6.5c.6-.6 1.3-.5 1.7.1l.9 1.4c.3.5.2 1-.2 1.4l-.5.5c.6 1.3 1.6 2.3 2.9 2.9l.5-.5c.4-.4.9-.5 1.4-.2l1.4.9c.6.4.7 1.1.1 1.7-1 1-2.4 1.2-3.9.4-2.1-1.1-3.8-2.8-4.9-4.9-.8-1.5-.6-2.9.4-3.9z" fill="#0c1e30"/></svg>
      <span class="call-word">Call</span><span class="call-num">800-Stormfix</span>
      <span class="call-alt">
        <svg width="22" height="22" viewBox="0 0 22 22"><circle cx="11" cy="11" r="10" fill="none" stroke="#0c1e30" stroke-width="2"/><path d="M7.5 6.5c.6-.6 1.3-.5 1.7.1l.9 1.4c.3.5.2 1-.2 1.4l-.5.5c.6 1.3 1.6 2.3 2.9 2.9l.5-.5c.4-.4.9-.5 1.4-.2l1.4.9c.6.4.7 1.1.1 1.7-1 1-2.4 1.2-3.9.4-2.1-1.1-3.8-2.8-4.9-4.9-.8-1.5-.6-2.9.4-3.9z" fill="#0c1e30"/></svg>
        <span class="call-or">or</span><span class="call-pre">800-</span><span class="call-help">Need Help?</span>
      </span>
    </div>

    <div class="website">www.<b>theclaimwardengroup</b>.com</div>

    <svg class="feature" viewBox="0 0 330 385">
      <defs>
        <linearGradient id="feature-photo" x1="0" y1="0" x2="0.3" y2="1">
          <stop offset="0" stop-color="#7a3cf0"/>
          <stop offset="0.5" stop-color="#5b1fd6"/>
          <stop offset="1" stop-color="#0d0220"/>
        </linearGradient>
      </defs>
      <rect x="4" y="4" width="322" height="377" rx="40" fill="#009ee3"/>
      <rect x="26" y="26" width="278" height="333" rx="26" fill="#ffffff"/>
      <rect x="34" y="34" width="262" height="317" rx="20" fill="url(#feature-photo)" role="img" aria-label="Lightning bolt striking above a house rooftop at night"/>
    </svg>
  </div>
</body>
</html>
```